modern stationary for real estate investment company
Varnek Properties
modern stationary for real estate investment company - Real Estate
Creative Brief
Professional
Marisol Dunleavy
President
no address
marisol@varnekproperties.ca
www.varnekproperties.ca
- Buy, renovate, sell and rent - Residential Properties - Wholesale Investor Program - First time home-buyer programs - Pay ca$h rewards for referrals - Private money investor programs with 8-12% returns
Teodor2017 Teodor2017

```html
<!DOCTYPE html>
<html lang="en">
<head>
<meta charset="utf-8">
<title>Varnek Properties – Business Cards</title>
<link rel="stylesheet" href="https://fonts.googleapis.com/css2?family=Cinzel:wght@500&family=Open+Sans:wght@400;700&display=swap">
<style>
  :root {
    --page: #e9e6e1;
    --ink: #0b0b0b;
    --paper: #ffffff;
    --orange: #f39a1e;
    --orange-deep: #e0761a;
    --blue: #2a73b8;
    --text-light: #f2f2f2;
    --text-dark: #1a2a44;
  }
  * { box-sizing: border-box; margin: 0; padding: 0; }
  html, body { width: 1200px; height: 911px; overflow: hidden; }
  body { background: var(--page); position: relative; font-family: "Open Sans", sans-serif; }

  .card {
    position: absolute;
    width: 640px;
    height: 366px;
    border-radius: 4px;
    overflow: hidden;
    box-shadow: 0 10px 28px rgba(0,0,0,.22);
  }
  .card--back { left: 110px; top: 60px; background: var(--ink); }
  .card--front { left: 450px; top: 480px; background: var(--paper); }

  .brand { display: flex; flex-direction: column; align-items: center; }
  .brand__dot { width: 44px; height: 44px; border-radius: 50%; background: var(--orange); margin-bottom: 10px; }
  .brand__name { font-family: "Cinzel", serif; font-weight: 500; letter-spacing: .5px; }

  .card--back .brand { position: absolute; top: 56px; left: 0; right: 0; }
  .card--back .brand__name { color: var(--text-light); font-size: 27px; }

  .services {
    position: absolute; top: 170px; left: 0; right: 0;
    list-style: none; text-align: center;
    color: var(--text-light); font-size: 12.5px; line-height: 1.55;
  }
  .services li::before { content: "*"; }

  .swoosh { position: absolute; inset: 0; }

  .card--front .brand { position: absolute; top: 26px; left: 0; right: 0; }
  .card--front .brand__dot { width: 38px; height: 38px; margin-bottom: 6px; }
  .card--front .brand__name { color: var(--text-dark); font-size: 23px; }

  .contact {
    position: absolute; right: 26px; top: 160px;
    list-style: none; color: var(--text-light); font-size: 12px; line-height: 1.75;
  }
  .contact li { display: flex; align-items: center; justify-content: flex-end; gap: 7px; }
  .contact svg { width: 11px; height: 11px; fill: var(--text-light); }

  .person { position: absolute; left: 30px; bottom: 26px; color: var(--text-light); }
  .person__name { font-weight: 700; font-size: 25px; line-height: 1.1; }
  .person__title { font-size: 15px; }
</style>
</head>
<body>

<section class="card card--back">
  <div class="brand">
    <span class="brand__dot"></span>
    <span class="brand__name">Varnek Properties</span>
  </div>
  <ul class="services">
    <li>buy, renovate, sell, and rent</li>
    <li>residential properties *wholesale investor properties</li>
    <li>pay cash rewards for referrals</li>
    <li>private money investor programs with 8-12% returns</li>
  </ul>
</section>

<section class="card card--front">
  <svg class="swoosh" viewBox="0 0 640 366" aria-hidden="true">
    <path d="M30 215 C 270 280, 380 100, 640 -5" fill="none" stroke="var(--blue)" stroke-width="4"/>
    <path d="M20 230 C 270 298, 385 112, 640 8" fill="none" stroke="var(--orange)" stroke-width="14"/>
    <path d="M30 236 C 270 300, 385 118, 640 16" fill="none" stroke="var(--orange-deep)" stroke-width="4"/>
    <path d="M0 240 C 260 310, 380 130, 640 26 L640 366 L0 366 Z" fill="var(--ink)"/>
  </svg>

  <div class="brand">
    <span class="brand__dot"></span>
    <span class="brand__name">Varnek Properties</span>
  </div>

  <ul class="contact">
    <li>613-555-0172
      <svg viewBox="0 0 24 24"><path d="M6.6 10.8a15 15 0 0 0 6.6 6.6l2.2-2.2a1 1 0 0 1 1-.25 11.4 11.4 0 0 0 3.6.57 1 1 0 0 1 1 1V20a1 1 0 0 1-1 1A17 17 0 0 1 3 4a1 1 0 0 1 1-1h3.5a1 1 0 0 1 1 1c0 1.25.2 2.45.57 3.6a1 1 0 0 1-.25 1z"/></svg>
    </li>
    <li>marisol@varnekproperties.ca
      <svg viewBox="0 0 24 24"><path d="M2 5h20v14H2z M4 7l8 6 8-6v-.01H4z" fill-rule="evenodd"/></svg>
    </li>
    <li>www.varnekproperties.ca
      <svg viewBox="0 0 24 24"><circle cx="12" cy="12" r="10"/></svg>
    </li>
  </ul>

  <div class="person">
    <p class="person__name">Marisol Dunleavy</p>
    <p class="person__title">President</p>
  </div>
</section>

</body>
</html>
```